Brindle's Botanic's. I make and sell organic bath & body products. Nourishing bath & body products. Products are soaps, scrubs, lip balms, bath salts, baby & mother products (belly balm, nipple balm, diaper balm, baby bath soak, chest rub,) . I use botanical and or herbs in all my recipes. I create my own recipes. I like muted colors...but I would like something that will get your attention. I like the colors green and brown, but open to any other colors. I would also like to get information about labels (different sizes for my products) I do like the pasley print and maybe even a cute owl.

Target Market(s)

women, pregnant and nursing women, women with children and men

Industry/Entity Type

Baby

Contact Information for Business Card

Mona Greeley
517-384-2706,mgreeley@tallowmail.example
mgreeley@tallowmail.example

Font styles to use
Other font styles liked:
• bree

Requirements
Must have
• Brindle's Botanic's, nourishing bath & body products. It needs to get a person attention. I would like to see cards that are hip and fun. I would also like to view cards that are classy. I do like muted colors but I do have an open mind (use any color you think would be right) So far a lot of the cards have had leaves....I really do not like that design.
Nice to have
• ???pasley in the background ?cute owl
Should not have
• leaves

```html
<!DOCTYPE html>
<html lang="en">
<head>
<meta charset="utf-8">
<title>Brindle's Botanic's — Business Card</title>
<link rel="stylesheet" href="https://fonts.googleapis.com/css2?family=Cinzel:wght@500;600&family=Gelasio:wght@400;700&display=swap">
<style>
  :root {
    --page: #ffffff;
    --kraft-light: #e7c38f;
    --kraft-mid: #d9ad72;
    --kraft-edge: #b98c56;
    --ink: #2e1f17;
    --ornament: #6e5750;
    --green-1: #4fae14;
    --green-2: #62c423;
    --green-3: #79dc30;
    --green-4: #93e65a;
  }
  * { margin: 0; padding: 0; box-sizing: border-box; }
  html, body {
    width: 1200px; height: 702px; overflow: hidden;
    background: var(--page);
  }
  .card {
    position: absolute; left: 57px; top: 57px;
    width: 1083px; height: 586px; overflow: hidden;
    background:
      radial-gradient(ellipse at 45% 40%, var(--kraft-light) 0%, var(--kraft-mid) 65%, var(--kraft-edge) 100%);
    color: var(--ink);
  }
  .waves { position: absolute; inset: 0; width: 100%; height: 100%; }
  .brand-name {
    position: absolute; left: 0; right: 0; top: 64px;
    text-align: center;
    font-family: "Cinzel", serif; font-weight: 500;
    font-size: 52px; font-variant: small-caps; letter-spacing: 2px;
  }
  .tagline {
    position: absolute; top: 178px; left: 72px; width: 946px; height: 46px;
  }
  .tagline .rule {
    position: absolute; bottom: 0; height: 3px; background: var(--ink);
  }
  .tagline .rule-left { left: 0; width: 437px; }
  .tagline .rule-right { left: 480px; width: 466px; }
  .tagline .words {
    position: absolute; bottom: 7px;
    font-family: "Gelasio", serif; font-size: 28px;
  }
  .tagline .words-left { right: 510px; }
  .tagline .words-right { left: 486px; }
  .tagline .amp {
    position: absolute; left: 442px; bottom: -12px;
    font-family: "Gelasio", serif; font-weight: 700; font-size: 36px;
  }
  .person-name {
    position: absolute; left: 0; right: 0; top: 278px;
    text-align: center;
    font-family: "Cinzel", serif; font-weight: 600;
    font-size: 30px; font-variant: small-caps; letter-spacing: 1px;
  }
  .ornament {
    position: absolute; left: 502px; top: 365px; width: 84px; height: 150px;
    background: radial-gradient(ellipse at center, var(--ornament) 0%, rgba(110,87,80,0.55) 45%, rgba(110,87,80,0) 72%);
  }
  .contact {
    position: absolute; left: 30px; top: 408px; list-style: none;
    font-family: "Cinzel", serif; font-weight: 600;
    font-size: 25px; font-variant: small-caps;
  }
  .contact li { display: flex; align-items: center; height: 38px; }
  .contact svg { width: 28px; height: 24px; margin-right: 14px; fill: var(--ink); }
  .contact .email { font-size: 22px; }
</style>
</head>
<body>
  <div class="card">
    <svg class="waves" viewBox="0 0 980 530" preserveAspectRatio="none" aria-hidden="true">
      <path fill="var(--green-1)" d="M0,398 C120,470 260,520 420,512 C640,500 800,260 980,216 L980,530 L0,530 Z"/>
      <path fill="var(--green-2)" d="M0,420 C140,490 300,525 460,518 C660,505 820,300 980,282 L980,530 L0,530 Z"/>
      <path fill="var(--green-3)" d="M0,446 C160,505 330,530 500,522 C700,510 850,350 980,338 L980,530 L0,530 Z"/>
      <path fill="var(--green-4)" d="M0,472 C180,520 360,532 540,526 C740,515 870,420 980,408 L980,530 L0,530 Z"/>
    </svg>

    <h1 class="brand-name">Brindle's Botanic's</h1>

    <div class="tagline">
      <span class="rule rule-left"></span>
      <span class="rule rule-right"></span>
      <span class="words words-left">organic bath</span>
      <span class="amp">&amp;</span>
      <span class="words words-right">body products</span>
    </div>

    <p class="person-name">Mona Greeley</p>

    <div class="ornament" role="img" aria-label="Decorative brown petal flourish"></div>

    <ul class="contact">
      <li>
        <svg viewBox="0 0 28 24" aria-hidden="true">
          <path d="M4,3 L9,2 L11,8 L8,10 C9,13 10,15 12,16 L15,14 L19,19 L15,22 C8,21 3,12 4,3 Z"/>
          <path d="M18,7 a5,5 0 0 1 0,8" fill="none" stroke="var(--ink)" stroke-width="2"/>
          <path d="M22,4 a9,9 0 0 1 0,14" fill="none" stroke="var(--ink)" stroke-width="2"/>
        </svg>
        <span>517-384-2706</span>
      </li>
      <li>
        <svg viewBox="0 0 28 24" aria-hidden="true">
          <rect x="1" y="4" width="26" height="17" rx="2"/>
          <path d="M2,5 L14,14 L26,5" fill="none" stroke="var(--kraft-light)" stroke-width="2"/>
        </svg>
        <span class="email">mgreeley@tallowmail.example</span>
      </li>
    </ul>
  </div>
</body>
</html>
```